B2B Umbrella Site Requires Simple, Stylish Slider Designs

We're a dynamic promotional merchandise business in the process of building a new B2B Umbrella Store. It's our goal to provide printed umbrellas to suit the needs of our clients. Our main page is in need of ONE large key banner and THREE smaller sub category banners. We would like to see designs that use grey and green (or similar) to match with the theme of our layout. See: http://canopyharbor.com.au/

The final designs should convey the desirability of our umbrellas while looking slick and modern in style. Please find attached our place holder banners for size reference and umbrella images to use in designs. If you require any further details or content, feel free to contact us.

Target Market(s)

Professionals and businesses across a wide range of fields. We offer a customisable product so we are as flexible as our target market.

Industry/Entity Type

Building

Font styles to use
Sans Serif

Requirements
Must have
• Must match sizes of attached sample graphics (
sub_banner + main_banner images). Must feature umbrella images attached to the brief - pick which images suit your design, but please ensure they are the correct umbrella style for the banner text. Clear, stylish text based on existing text found on sample graphics.
Nice to have
• Colours similar to the ones existing on the website already.
Should not have
• No serif fonts or clipart. Colours that do not facilitate easy reading.

```html
<!DOCTYPE html>
<html lang="en">
<head>
<meta charset="utf-8">
<title>Canopy Harbor – Promotional Umbrella Banners</title>
<link rel="stylesheet" href="https://fonts.googleapis.com/css2?family=Bebas+Neue&family=Oswald:wght@300&display=swap">
<style>
  :root {
    --grey-light: #f3f3f3;
    --grey-mid: #e4e4e4;
    --grey-dark: #cfcfcf;
    --page: #ffffff;
    --green-deep: #10692f;
    --green: #1f9e48;
    --green-bright: #2db553;
    --label-grey: #4a4a4a;
    --white: #ffffff;
  }
  * { margin: 0; padding: 0; box-sizing: border-box; }
  html, body { width: 1200px; height: 724px; overflow: hidden; background: var(--page); }
  .canvas { position: relative; width: 1200px; height: 724px; }

  .main-banner {
    position: absolute; left: 0; top: 0; width: 1200px; height: 492px; overflow: hidden;
    background: linear-gradient(165deg, var(--grey-light) 0%, #ebebeb 50%, var(--grey-dark) 100%);
  }
  .main-banner > svg { position: absolute; left: 0; top: 0; }

  .hero-photo {
    position: absolute; left: 500px; top: 0; width: 660px; height: 485px;
    background:
      radial-gradient(ellipse 38% 42% at 55% 42%, rgba(23,166,78,0.55) 0%, rgba(23,166,78,0.25) 55%, rgba(23,166,78,0) 100%),
      radial-gradient(ellipse 50% 50% at 50% 45%, rgba(255,255,255,0.55) 0%, rgba(255,255,255,0) 100%);
  }

  .hero-text .kicker { font-family: 'Oswald', sans-serif; font-weight: 300; fill: var(--white); }
  .hero-text .headline,
  .hero-text .subline { font-family: 'Bebas Neue', sans-serif; fill: var(--white); }

  .sub-banner {
    position: absolute; top: 510px; width: 388px; height: 214px; overflow: hidden;
    background: linear-gradient(165deg, var(--grey-light) 0%, var(--grey-mid) 55%, var(--grey-dark) 100%);
  }
  .sub-banner.corporate { left: 0; }
  .sub-banner.folding { left: 408px; }
  .sub-banner.golf { left: 812px; }
  .sub-photo { position: absolute; left: 110px; top: 0; width: 278px; height: 214px; }
  .corporate .sub-photo { background: radial-gradient(ellipse 55% 55% at 55% 40%, rgba(45,46,122,0.55) 0%, rgba(45,46,122,0.2) 60%, rgba(45,46,122,0) 100%); }
  .folding .sub-photo { background: radial-gradient(ellipse 55% 50% at 55% 35%, rgba(22,26,34,0.5) 0%, rgba(22,26,34,0.18) 60%, rgba(22,26,34,0) 100%); }
  .golf .sub-photo { background: radial-gradient(ellipse 55% 55% at 60% 40%, rgba(18,58,35,0.55) 0%, rgba(18,58,35,0.2) 60%, rgba(18,58,35,0) 100%); }
  .sub-banner > svg { position: absolute; left: 0; top: 0; }
  .sub-title .label { font-family: 'Oswald', sans-serif; font-weight: 300; font-size: 16px; fill: var(--label-grey); }
  .sub-title .name { font-family: 'Bebas Neue', sans-serif; font-size: 50px; }
</style>
</head>
<body>
<div class="canvas">

  <section class="main-banner">
    <svg width="1200" height="492" aria-hidden="true">
      <path d="M0 440 Q520 310 1200 370 L1200 392 Q520 340 0 478 Z" fill="#ffffff" opacity="0.45"/>
      <path d="M320 0 Q720 120 1200 60 L1200 22 Q720 92 380 0 Z" fill="#ffffff" opacity="0.4"/>
    </svg>

    <div class="hero-photo" role="img" aria-label="Photo of an open green and white panelled promotional umbrella with a wooden handle"></div>

    <svg class="hero-text" width="1200" height="492" role="presentation">
      <defs>
        <linearGradient id="ribbonFill" x1="0" y1="0" x2="0" y2="1">
          <stop offset="0" stop-color="#0f6b33"/>
          <stop offset="1" stop-color="#2db553"/>
        </linearGradient>
      </defs>
      <polygon points="0,155 547,155 694,366 0,366" fill="url(#ribbonFill)"/>
      <rect x="0" y="379" width="696" height="2" fill="#1f9e48"/>
      <rect x="0" y="387" width="696" height="2" fill="#1f9e48"/>
      <text class="kicker" x="126" y="195" font-size="37" textLength="278" lengthAdjust="spacingAndGlyphs">AUSTRALIA’S TOP</text>
      <text class="headline" x="46" y="287" font-size="112" textLength="483" lengthAdjust="spacingAndGlyphs">PROMOTIONAL</text>
      <text class="subline" x="46" y="357" font-size="86" textLength="483" lengthAdjust="spacingAndGlyphs">UMBRELLA VENDOR</text>
    </svg>
  </section>

  <section class="sub-banner corporate">
    <div class="sub-photo" role="img" aria-label="Photo of a navy blue medium corporate umbrella"></div>
    <svg class="sub-title" width="388" height="214" role="presentation">
      <defs>
        <linearGradient id="nameFillA" x1="0" y1="0" x2="0" y2="1">
          <stop offset="0" stop-color="#2db553"/><stop offset="1" stop-color="#10692f"/>
        </linearGradient>
      </defs>
      <text class="label" x="16" y="90" textLength="44" lengthAdjust="spacingAndGlyphs">MEDIUM</text>
      <text class="name" x="16" y="130" fill="url(#nameFillA)" textLength="164" lengthAdjust="spacingAndGlyphs">CORPORATE</text>
      <text class="name" x="16" y="170" fill="url(#nameFillA)" textLength="164" lengthAdjust="spacingAndGlyphs">UMBRELLAS</text>
      <rect x="0" y="176" width="213" height="2" fill="#1f9e48"/>
      <rect x="0" y="183" width="213" height="2" fill="#1f9e48"/>
    </svg>
  </section>

  <section class="sub-banner folding">
    <div class="sub-photo" role="img" aria-label="Photo of a black portable folding umbrella"></div>
    <svg class="sub-title" width="388" height="214" role="presentation">
      <defs>
        <linearGradient id="nameFillB" x1="0" y1="0" x2="0" y2="1">
          <stop offset="0" stop-color="#2db553"/><stop offset="1" stop-color="#10692f"/>
        </linearGradient>
      </defs>
      <text class="label" x="16" y="90" textLength="80" lengthAdjust="spacingAndGlyphs">PORTABLE</text>
      <text class="name" x="16" y="130" fill="url(#nameFillB)" textLength="114" lengthAdjust="spacingAndGlyphs">FOLDING</text>
      <text class="name" x="16" y="170" fill="url(#nameFillB)" textLength="163" lengthAdjust="spacingAndGlyphs">UMBRELLAS</text>
      <rect x="0" y="176" width="213" height="2" fill="#1f9e48"/>
      <rect x="0" y="183" width="213" height="2" fill="#1f9e48"/>
    </svg>
  </section>

  <section class="sub-banner golf">
    <div class="sub-photo" role="img" aria-label="Photo of a dark green popular golf umbrella"></div>
    <svg class="sub-title" width="388" height="214" role="presentation">
      <defs>
        <linearGradient id="nameFillC" x1="0" y1="0" x2="0" y2="1">
          <stop offset="0" stop-color="#2db553"/><stop offset="1" stop-color="#10692f"/>
        </linearGradient>
      </defs>
      <text class="label" x="16" y="90" textLength="73" lengthAdjust="spacingAndGlyphs">POPULAR</text>
      <text class="name" x="16" y="130" fill="url(#nameFillC)" textLength="55" lengthAdjust="spacingAndGlyphs">GOLF</text>
      <text class="name" x="16" y="170" fill="url(#nameFillC)" textLength="172" lengthAdjust="spacingAndGlyphs">UMBRELLAS</text>
      <rect x="0" y="176" width="213" height="2" fill="#1f9e48"/>
      <rect x="0" y="183" width="213" height="2" fill="#1f9e48"/>
    </svg>
  </section>

</div>
</body>
</html>
```